Fenwell Building Partners Stationary Revamp

We need a full set of new stationary including business cards for our Public Sector Construction company based in the South East of England. We have a new logo (attached) that we want to launch and revamp all of our company literature. We are required to send a lot of correspondence to residents etc so a consistent theme is required across everything. Also attached is our existing templates.

Target Market(s)

We work for Council and government provided housing organisations and NOT private individuals. All of our clients represent government spent money, so we need to look professional and instantly recognisable brand.

Industry/Entity Type

Business

Colors

Designer to choose colors to be used in the design.

Requirements
Must have
• New fresh designs that utilise our new logo. And the letterhead needs to be able to be rolled out onto a word template so that all staff can type straight onto it rather than us having to have it printed first.
Nice to have
• I am looking forward to seeing your best efforts as designers.

```html
<!DOCTYPE html>
<html lang="en">
<head>
<meta charset="utf-8">
<title>Fenwell Building Partners – Business Card</title>
<link href="https://fonts.googleapis.com/css2?family=Roboto:wght@400;500&display=swap" rel="stylesheet">
<style>
  :root {
    --page-bg: #d8d5d1;
    --card-frost: #ecebea;
    --card-frost-edge: #d9d8d6;
    --card-dark: #151313;
    --gold: #c9961f;
    --gold-light: #f1cf63;
    --gold-deep: #8f6410;
    --ink: #1c1a18;
    --text-light: #dedad6;
    --text-muted: #b9b4ae;
    --postcode: #e4a98a;
  }
  * { margin: 0; padding: 0; box-sizing: border-box; }
  html, body {
    width: 1200px; height: 969px; overflow: hidden;
    background: var(--page-bg);
    font-family: "Roboto", Arial, sans-serif;
  }
  .business-card {
    position: absolute; left: 100px; top: 199px;
    width: 1000px; height: 571px;
    border-radius: 28px; overflow: hidden;
    background: linear-gradient(160deg, var(--card-frost), var(--card-frost-edge));
    box-shadow: 0 10px 30px rgba(0,0,0,0.18);
  }
  .card-artwork { position: absolute; inset: 0; width: 100%; height: 100%; }
  .company-name {
    position: absolute; left: 0; width: 910px; top: 202px;
    text-align: center; font-size: 34px; font-weight: 500;
    color: var(--ink); letter-spacing: 0.5px;
  }
  .contact-person {
    position: absolute; right: 55px; top: 326px; text-align: right;
  }
  .person-name {
    font-size: 32px; font-weight: 500; color: var(--gold); letter-spacing: 1px;
  }
  .person-role {
    margin-top: 4px; font-size: 25px; color: var(--text-muted); letter-spacing: 1.5px;
  }
  .contact-list {
    position: absolute; right: 58px; top: 409px; list-style: none;
  }
  .contact-list li {
    display: flex; justify-content: flex-end; align-items: center;
    height: 32px; font-size: 23px; color: var(--text-light);
  }
  .contact-list svg { width: 20px; height: 20px; margin-left: 20px; fill: var(--gold); }
  .company-address {
    position: absolute; left: 47px; top: 436px;
    font-size: 23px; line-height: 32px; color: var(--text-light); font-style: normal;
  }
  .postcode { color: var(--postcode); }
  .registration { color: var(--text-muted); }
  .registration span { color: var(--text-light); }
</style>
</head>
<body>
  <div class="business-card">
    <svg class="card-artwork" viewBox="0 0 1000 571" preserveAspectRatio="none" aria-hidden="true">
      <defs>
        <linearGradient id="goldBand" x1="0" y1="0" x2="1" y2="0">
          <stop offset="0" stop-color="#b07e15"/>
          <stop offset="0.35" stop-color="#f1cf63"/>
          <stop offset="0.6" stop-color="#c9961f"/>
          <stop offset="0.85" stop-color="#f4d470"/>
          <stop offset="1" stop-color="#9c6e12"/>
        </linearGradient>
        <linearGradient id="darkBase" x1="0" y1="0" x2="1" y2="1">
          <stop offset="0" stop-color="#2a2624"/>
          <stop offset="0.5" stop-color="#151313"/>
          <stop offset="1" stop-color="#0c0b0b"/>
        </linearGradient>
        <linearGradient id="silverSwoosh" x1="0" y1="0" x2="1" y2="0">
          <stop offset="0" stop-color="#ffffff" stop-opacity="0.3"/>
          <stop offset="0.5" stop-color="#ffffff" stop-opacity="0.95"/>
          <stop offset="1" stop-color="#ffffff" stop-opacity="0.2"/>
        </linearGradient>
      </defs>
      <path class="gold-band" d="M0,112 C220,300 620,330 1000,135 L1000,172 C660,345 300,335 0,228 Z" fill="url(#goldBand)"/>
      <path class="dark-base" d="M0,228 C300,335 660,345 1000,172 L1000,571 L0,571 Z" fill="url(#darkBase)"/>
      <path class="silver-swoosh" d="M28,268 C150,350 320,385 480,384 C320,372 160,342 28,268 Z" fill="url(#silverSwoosh)"/>
    </svg>

    <div class="company-name">Fenwell Building Partners</div>

    <div class="contact-person">
      <div class="person-name">R T MARLOW MIOD</div>
      <div class="person-role">MANAGING DIRECTOR</div>
    </div>

    <ul class="contact-list">
      <li>020 7946 0312
        <svg viewBox="0 0 24 24"><path d="M6.6 10.8a15 15 0 0 0 6.6 6.6l2.2-2.2a1 1 0 0 1 1-.25 11.4 11.4 0 0 0 3.6.57 1 1 0 0 1 1 1V20a1 1 0 0 1-1 1A17 17 0 0 1 3 4a1 1 0 0 1 1-1h3.5a1 1 0 0 1 1 1c0 1.25.2 2.45.57 3.57a1 1 0 0 1-.25 1z"/></svg>
      </li>
      <li>020 7946 0318
        <svg viewBox="0 0 24 24"><path d="M6 2h12v5H6zM3 8h18a2 2 0 0 1 2 2v7h-4v5H5v-5H1v-7a2 2 0 0 1 2-2zm4 8v4h10v-4z"/></svg>
      </li>
      <li>info@fenwellbp.co.uk
        <svg viewBox="0 0 24 24"><path d="M2 5h20v14H2zm2 2v.5l8 5 8-5V7z"/></svg>
      </li>
      <li>www.fenwellbp.co.uk
        <svg viewBox="0 0 24 24"><path d="M12 2a10 10 0 1 0 0 20 10 10 0 0 0 0-20zm-1 17.9A8 8 0 0 1 4.1 10.6L9 15.5v1a2 2 0 0 0 2 2zm6.9-2.5A2 2 0 0 0 16 16h-1v-3a1 1 0 0 0-1-1H8v-2h2a1 1 0 0 0 1-1V7h2a2 2 0 0 0 2-2v-.4a8 8 0 0 1 2.9 12.8z"/></svg>
      </li>
    </ul>

    <address class="company-address">
      Harlow House, 12 Brookfield Road<br>
      Maidstone, Kent, <span class="postcode">ME14 2QL</span><br>
      <span class="registration">Registration number: <span>08127749</span></span>
    </address>
  </div>
</body>
</html>
```